Business card design for engineering firm specializing in defense industry.

We need a professional business card design. Something simple but stands out. We are an engineering company specializing in composites in the defense industry.
Industry/Entity Type
Defense
Contact Information for Business Card
A simple black business card with the Varlonix yellow color is what we had in mind but open for other designs.
Colors
ffc214

```html
<!DOCTYPE html>
<html lang="en">
<head>
<meta charset="utf-8">
<title>Varlonix Business Card</title>
<link rel="stylesheet" href="https://fonts.googleapis.com/css2?family=Lato:wght@400;700;900&display=swap">
<style>
  :root {
    --brand-yellow: #ffc214;
    --card-yellow: #fdbf00;
    --ink: #111111;
    --paper: #ffffff;
    --backdrop: #dcdcdc;
  }
  * { box-sizing: border-box; margin: 0; padding: 0; }
  html, body {
    width: 1200px;
    height: 900px;
    overflow: hidden;
  }
  body {
    background: var(--backdrop);
    font-family: "Lato", Arial, sans-serif;
    position: relative;
  }
  .card {
    position: absolute;
    width: 520px;
    height: 298px;
    border-radius: 26px;
    overflow: hidden;
  }
  .card--front {
    left: 110px;
    top: 130px;
    background: var(--card-yellow);
    display: flex;
    align-items: center;
    justify-content: center;
  }
  .card--back {
    left: 580px;
    top: 450px;
    background: var(--paper);
  }
  .wordmark {
    display: flex;
    align-items: center;
    gap: 12px;
  }
  .wordmark__mark {
    width: 18px;
    height: 18px;
  }
  .wordmark__name {
    font-weight: 900;
    font-size: 58px;
    letter-spacing: 1px;
    line-height: 1;
  }
  .card--front .wordmark__mark { background: var(--ink); }
  .card--front .wordmark__name { color: var(--ink); }

  .card--back .wordmark {
    position: absolute;
    left: 34px;
    top: 62px;
  }
  .card--back .wordmark__mark { background: var(--brand-yellow); }
  .card--back .wordmark__name { color: var(--ink); font-size: 52px; }

  .identity {
    position: absolute;
    left: 34px;
    bottom: 30px;
    font-size: 16px;
    line-height: 1.2;
    color: var(--ink);
  }
  .identity__name,
  .identity__company {
    color: var(--brand-yellow);
    font-size: 18px;
    text-transform: uppercase;
  }
  .identity__company { margin-top: 6px; }

  .contacts {
    position: absolute;
    right: 30px;
    top: 150px;
    list-style: none;
    font-size: 14px;
    line-height: 1.45;
    color: var(--ink);
    text-align: right;
  }
  .contacts__item {
    display: flex;
    align-items: center;
    justify-content: flex-end;
    gap: 6px;
  }
  .contacts__icon {
    width: 12px;
    height: 12px;
    flex: none;
  }
</style>
</head>
<body>

  <section class="card card--front" aria-label="Business card front">
    <div class="wordmark">
      <span class="wordmark__mark"></span>
      <span class="wordmark__name">Varlonix</span>
    </div>
  </section>

  <section class="card card--back" aria-label="Business card back">
    <div class="wordmark">
      <span class="wordmark__mark"></span>
      <span class="wordmark__name">Varlonix</span>
    </div>

    <ul class="contacts">
      <li class="contacts__item">044-987 210 345
        <svg class="contacts__icon" viewBox="0 0 12 12" aria-hidden="true">
          <path d="M2 1.5h2.2l1 2.4-1.3 1c.7 1.4 1.8 2.5 3.2 3.2l1-1.3 2.4 1V10c0 .6-.5 1-1 1C5.2 11 1 6.8 1 2.5c0-.5.4-1 1-1z" fill="#ffc214"/>
        </svg>
      </li>
      <li class="contacts__item">info@varlonix.com
        <svg class="contacts__icon" viewBox="0 0 12 12" aria-hidden="true">
          <rect x="1" y="2.5" width="10" height="7" rx="1" fill="#ffc214"/>
          <path d="M1.5 3l4.5 3.5L10.5 3" stroke="#fff" stroke-width="1" fill="none"/>
        </svg>
      </li>
      <li class="contacts__item">www.varlonixinc.com
        <svg class="contacts__icon" viewBox="0 0 12 12" aria-hidden="true">
          <circle cx="6" cy="6" r="5" fill="#ffc214"/>
          <path d="M1 6h10M6 1c-2 2.5-2 7.5 0 10M6 1c2 2.5 2 7.5 0 10" stroke="#fff" stroke-width=".8" fill="none"/>
        </svg>
      </li>
    </ul>

    <div class="identity">
      <p class="identity__name">Daniel Marsh</p>
      <p class="identity__title">Managing Director</p>
      <p class="identity__company">Varlonix, Inc.</p>
      <p class="identity__street">28 Harbor Avenue</p>
      <p class="identity__city">Dover, Maine 04418</p>
    </div>
  </section>

</body>
</html>
```